Brightfold Reach - B2B Demand Generation Website Project

We need a fully functional website for www.brightfoldreach-example.com. We are a B2B Demand Generation company, based in London, working with companies such as QTR, DWN, Vortan, Brelloway, Pelta generating them sales leads for their sales teams. We run this through digital marketing newsletter promotions and have a network of websites. Content syndication, data, demand generation, online marketing. Our logo has just been redone (attached) and we have a holding page already which i would like to use the style / colours. Our logo is bright and vibrant but i dont want the site to be a rainbow. We are expensive, classy, professorial, B2B, intelligent.

Home
About Us
Our Services
Prospero & QA Technology
Intent Data
Testimonials
Contact Us

Target Market(s)

B2B Marketers (QTR, Quorvane, Pelta, DWN, Vista Hub, Harrowby, Tremont Axis, Technology Companies, Data Companies, Marketing Teams, Cloudwick.

Industry/Entity Type

Marketing

Coding

Coded - Design and coding required

Number of Pages Required

5+ page

Font styles to use
Sans Serif

Requirements
Must have
• Home
About Us
Our Services
Prospero & QA Technology
Intent Data
Testimonials
Contact Us

Simple Pages.

Look classy, intelligent, data experts. I like the video homepages were the image moves at the top. Very soft animation.
Nice to have
• Websites i like:

https://www.dwn-example.com/
https://www.pulsegate-example.com/
https://www.lmsitecraft-example.co.uk/

Brightfold Reach - The Demand Generation Company
Should not have
• Pixelvault crap images

```html
<!DOCTYPE html>
<html lang="en">
<head>
<meta charset="utf-8">
<title>Brightfold Reach - The Demand Generation Company</title>
<link href="https://fonts.googleapis.com/css2?family=Comfortaa:wght@500;700&family=Open+Sans:ital,wght@0,400;0,600;0,700;1,400&display=swap" rel="stylesheet">
<style>
:root{
  --red:#d9272e;
  --blue:#1e56a0;
  --blue-deep:#143f86;
  --blue-bright:#2a6ac2;
  --navy:#171d2a;
  --ink:#3b3f46;
  --grey:#8a8f98;
  --line:#d8dbe0;
  --white:#fff;
}
*{box-sizing:border-box;margin:0;padding:0}
html,body{width:1200px;height:4932px;overflow:hidden}
body{font-family:"Open Sans",Arial,sans-serif;color:var(--ink);background:var(--white);position:relative}
section,header,footer{position:absolute;left:0;width:1200px}

/* top bar */
.topbar{top:0;height:29px;background:var(--red);color:#fff;font-size:13px;display:flex;justify-content:flex-end;align-items:center;gap:28px;padding-right:62px}
.topbar span{display:flex;align-items:center;gap:7px}
.site-header{top:29px;height:67px;background:#fff}
.brand{position:absolute;left:86px;top:20px;display:flex;align-items:center;gap:10px;font-family:"Comfortaa",sans-serif;font-size:22px;font-weight:700;color:var(--red)}
.brand i{width:14px;height:14px;border-radius:50%;background:var(--red);display:block}
.nav{position:absolute;left:300px;top:34px;display:flex;gap:46px;font-family:"Comfortaa",sans-serif;font-size:12.5px;color:#333}
.nav .home{color:var(--blue)}

/* hero */
.hero{top:96px;height:602px;background:radial-gradient(ellipse at 50% 40%,#2a66bb 0%,#1b4f9d 55%,#123b7e 100%)}
.hero h1{position:absolute;top:278px;width:100%;text-align:center;font-family:"Comfortaa",sans-serif;font-weight:500;font-size:46px;color:#fff;letter-spacing:.5px}
.dots{position:absolute;top:566px;left:0;width:100%;display:flex;justify-content:center;gap:12px}
.dots i{width:16px;height:16px;border-radius:50%;background:var(--red);display:block}
.dots i.on{background:#fff}

/* partners */
.partners{top:712px;height:70px;display:flex;gap:16px;padding-left:25px}
.partner{width:112px;height:60px;border:1px solid var(--line);display:flex;align-items:center;justify-content:center;font-weight:700;font-size:16px;color:#444}

/* intro */
.intro{top:822px;padding:0 96px;text-align:center;font-size:13px;line-height:20px;color:#444}

/* tickers */
.tickers{top:928px;height:180px}
.ticker{position:absolute;top:58px;width:278px;height:114px;border:1px solid var(--line);box-shadow:0 2px 4px rgba(0,0,0,.06)}
.ticker .badge{position:absolute;left:50%;top:-58px;margin-left:-60px;width:120px;height:120px;border-radius:50%;border:4px solid var(--blue);background:#fff;text-align:center;padding-top:30px;font-size:15px;color:#222;line-height:22px}
.ticker .badge b{display:block;color:var(--blue);font-size:19px}
.ticker p{position:absolute;bottom:14px;width:100%;text-align:center;color:var(--red);font-size:17px;font-weight:600}

/* section headings */
.heading{position:absolute;left:0;width:100%;display:flex;justify-content:center;align-items:center;gap:14px}
.heading h2{font-family:"Comfortaa",sans-serif;font-weight:700;font-size:29px;color:var(--blue)}
.rule{display:flex;align-items:center}
.rule span{width:110px;height:2px;background:var(--red);display:block}
.rule i{width:9px;height:9px;border-radius:50%;background:var(--red);display:block}

/* about */
.about{top:1192px;height:651px;background:linear-gradient(180deg,#1a2232,#151a26)}
.about .copy{position:absolute;top:165px;left:90px;width:1020px;text-align:center;color:#fff;font-size:13px;line-height:20px}
.about .copy p{margin-bottom:20px}
.feature{position:absolute;width:471px;height:48px;border:1.5px solid var(--red);border-radius:3px;color:#fff;font-size:14px;font-weight:600;display:flex;align-items:center;padding-left:24px}
.feature::before{content:"";width:6px;height:6px;border-radius:50%;background:#fff;margin-right:12px}

/* services */
.services{top:1843px;height:817px;background:#fff}
.card{position:absolute;top:209px;width:341px;height:484px;border:1px solid #dfe2e6;box-shadow:0 2px 6px rgba(0,0,0,.08);background:#fff;text-align:center}
.card .photo{margin:9px;height:200px}
.card .icon{position:absolute;left:50%;top:176px;margin-left:-28px;width:56px;height:56px;border-radius:50%;background:#fff;border:2px solid var(--red);display:flex;align-items:center;justify-content:center}
.card h3{margin-top:40px;font-family:"Comfortaa",sans-serif;font-weight:500;font-size:15px;color:var(--blue);white-space:nowrap}
.card p{margin:16px 24px 0;font-size:11.5px;line-height:17px;color:#444}
.btn-outline{position:absolute;left:50%;bottom:-16px;margin-left:-68px;width:136px;height:32px;background:#fff;border:1.5px solid var(--red);border-radius:3px;color:var(--red);font-size:13px;font-weight:600;display:flex;align-items:center;justify-content:center;gap:6px}
.btn-outline.muted{border-color:#bbb;color:#999}

/* qa */
.qa{top:2660px;height:584px;background:radial-gradient(ellipse at 40% 30%,#2660b3,#1a4c98 60%,#123b7c)}
.qa .heading h2,.testimonials .heading h2{color:#fff}
.qa .copy{position:absolute;left:98px;top:215px;width:690px;color:#fff;font-size:13px;line-height:19px}
.qa .copy p{margin-bottom:19px}
.btn-solid{display:inline-flex;align-items:center;gap:6px;height:34px;padding:0 14px;background:var(--blue-bright);border:1px solid #4f8ce0;border-radius:3px;color:#fff;font-size:13px;font-weight:600}
.product{position:absolute;left:831px;top:219px;width:290px;height:290px;border-radius:50%;background:#c9c9cb;display:flex;align-items:center;justify-content:center;font-size:44px;color:#3a3a3a;letter-spacing:4px}

/* intent */
.intent{top:3244px;height:622px;background:#fff}
.intent .photo{position:absolute;left:103px;top:151px;width:330px;height:330px;border-radius:50%;background:linear-gradient(135deg,#8e9cb2,#2d3d5c)}
.intent .head{position:absolute;left:525px;top:170px;display:flex;align-items:center;gap:12px}
.intent h2{font-family:"Comfortaa",sans-serif;font-weight:700;font-size:29px;color:var(--blue)}
.intent .copy{position:absolute;left:525px;top:240px;width:612px;font-size:13px;line-height:19px;color:#444}
.intent .copy p{margin-bottom:18px}
.intent .btn-solid{background:var(--blue);border-color:var(--blue)}

/* testimonials */
.testimonials{top:3866px;height:594px;background:linear-gradient(180deg,#3a2e2d,#231c1f 60%,#2c2426)}
.quote{position:absolute;top:230px;width:340px;height:172px;border:1.5px solid rgba(255,255,255,.7);border-radius:4px;padding:54px 20px 0;text-align:center;color:#fff;font-size:11.5px;line-height:18px;font-style:italic}
.quote .mark{position:absolute;left:50%;top:-26px;margin-left:-26px;width:52px;height:52px;border-radius:50%;background:var(--red);color:#fff;font-family:Georgia,serif;font-style:normal;font-size:40px;line-height:64px;font-weight:700}
.quote .who{position:absolute;top:190px;left:0;width:100%;font-style:normal;font-size:13px;line-height:19px}
.quote .who b{display:block;font-weight:700}

/* footer */
.site-footer{top:4460px;height:430px;background:#fff}
.col{position:absolute;top:83px}
.col h4{display:flex;align-items:center;gap:8px;font-family:"Comfortaa",sans-serif;font-weight:500;font-size:18px;color:var(--blue)}
.col h4 .rule span{width:44px}
.col ul{list-style:none;margin-top:32px;font-size:12.5px;color:#333}
.col li{height:30px;display:flex;align-items:center;gap:10px}
.col li::before{content:"";width:5px;height:5px;border-radius:50%;background:#333}
.contact-row{display:flex;gap:16px;font-size:12.5px;color:#333;line-height:18px;margin-bottom:26px}
.contact-row b{color:var(--red);font-weight:600;display:block}
.field{width:270px;height:26px;border:1px solid #bbb;font-size:11px;color:#666;padding:5px 6px;margin-bottom:11px}
.field.tall{height:42px}
.submit{width:126px;height:28px;background:var(--blue);color:#fff;font-weight:700;font-size:14px;display:flex;align-items:center;justify-content:center;gap:6px;border-radius:2px}
.social li::before{display:none}
.social li{height:56px;gap:12px}
.social i{width:28px;height:28px;border-radius:50%;border:1.5px solid var(--blue);display:block}
.copyright{top:4890px;height:42px;background:var(--blue);color:#fff;font-size:13px;display:flex;align-items:center;justify-content:center}
</style>
</head>
<body>

<div class="topbar" style="position:absolute;left:0;top:0;width:1200px">
  <span><svg width="13" height="13" viewBox="0 0 24 24"><path fill="#fff" d="M6.6 10.8a15 15 0 006.6 6.6l2.2-2.2a1 1 0 011-.25 11.4 11.4 0 003.6.6 1 1 0 011 1V20a1 1 0 01-1 1A17 17 0 013 4a1 1 0 011-1h3.5a1 1 0 011 1c0 1.25.2 2.45.6 3.6a1 1 0 01-.25 1z"/></svg>020-555-0147</span>
  <span><svg width="14" height="12" viewBox="0 0 24 20"><rect x="1" y="1" width="22" height="18" rx="2" fill="none" stroke="#fff" stroke-width="2"/><path d="M1 2l11 9 11-9" fill="none" stroke="#fff" stroke-width="2"/></svg>info@brightfoldreach-example.com</span>
</div>

<header class="site-header">
  <div class="brand"><i></i>brightfoldreach</div>
  <nav class="nav">
    <span class="home"><svg width="16" height="14" viewBox="0 0 24 20"><path d="M12 1L1 11h3v8h6v-6h4v6h6v-8h3z" fill="#1e56a0"/></svg></span>
    <span>About Us</span><span>Our Services</span><span>Prospero &amp; Qa Technology</span><span>Intent Data</span><span>Testimonials</span><span>Contact Us</span>
  </nav>
</header>

<section class="hero" role="img" aria-label="Blue background with a soft moving network of connected points">
  <h1>The Demand Generation Company</h1>
  <div class="dots"><i></i><i class="on"></i><i></i><i></i></div>
</section>

<section class="partners">
  <div class="partner">QTR</div><div class="partner">Pelta</div><div class="partner">DWN</div>
  <div class="partner">Halvern</div><div class="partner">Cirrusly</div><div class="partner">Meridane</div>
  <div class="partner">Taskmoor</div><div class="partner">Netrove</div><div class="partner">Camparo</div>
</section>

<section class="intro">
  <p>Brightfold Reach offers multi-channel demand generation services to publishers and technology vendors through our network of lead generation websites and native speaking telemarketing agents. Whether looking for MQL, ABM or BANT campaigns, Brightfold Reach can assist you in delivering your demand generation strategy and generate pipeline for your sales teams and/or channel partners.</p>
</section>

<section class="tickers">
  <div class="ticker" style="left:153px"><div class="badge">Ticker to<b>70,000+</b></div><p>Downloads Per Month</p></div>
  <div class="ticker" style="left:475px"><div class="badge">Ticker<b>25,000+</b></div><p>Leads Delivered Per Month</p></div>
  <div class="ticker" style="left:796px"><div class="badge">Ticker to<b>50+</b></div><p>Countries We Can Reach</p></div>
</section>

<section class="about">
  <div class="heading" style="top:108px">
    <div class="rule"><span></span><i></i></div><h2>About Us</h2><div class="rule"><i></i><span></span></div>
  </div>
  <div class="copy">
    <p>Brightfold Reach can deliver high quality sales leads from any country in the world. This can include leads via email or telemarketing, account-based targeting (ABM) or identifying need and pain points through BANT / SQL campaigns.</p>
    <p>Brightfold Reach offer expert demand generation support, from providing detailed leads of qualified decision-makers, to a comprehensive lead generation and SQL service.</p>
    <p>Our extensive and ongoing research campaigns give you the ability to build contact lists that identify individuals at all stages of the buying cycle, from pre-sales to sales ready.</p>
    <p>With access to over 31 million names, Brightfold Reach offers a range of marketing options that allow you to use our data to target the decision makers you need to reach.</p>
  </div>
  <div class="feature" style="left:109px;top:406px">Breakdown by geography, job title, role and responsibility</div>
  <div class="feature" style="left:616px;top:406px">Targeting through previous research and buying intention</div>
  <div class="feature" style="left:109px;top:483px">Email dispatch to selected individuals</div>
  <div class="feature" style="left:616px;top:483px">Extensive telemarketing options</div>
</section>

<section class="services">
  <div class="heading" style="top:110px">
    <div class="rule"><span></span><i></i></div><h2>Our Services</h2><div class="rule"><i></i><span></span></div>
  </div>
  <article class="card" style="left:86px">
    <div class="photo" role="img" aria-label="Business people reviewing charts beside a laptop" style="background:linear-gradient(135deg,#e4e6ea,#6b7078)"></div>
    <div class="icon"><svg width="26" height="26" viewBox="0 0 24 24"><rect x="3" y="4" width="15" height="12" fill="none" stroke="#1e56a0" stroke-width="2"/><circle cx="16" cy="15" r="4" fill="#fff" stroke="#d9272e" stroke-width="2"/><path d="M19 18l3 3" stroke="#d9272e" stroke-width="2"/></svg></div>
    <h3>Marketing Qualified Leads (MQL)</h3>
    <p>A Marketing Qualified Lead (MQL) is a prospect that has expressed an interest in what your brand has to offer. An MQL has taken the first steps to becoming a customer and is ready to receive additional contact from your company. From a very general perspective: Marketing Qualified Leads turn into Sales Qualified Leads (SQLs), which in turn can convert into customers once...</p>
    <div class="btn-outline muted">READ MORE <span>&#10230;</span></div>
  </article>
  <article class="card" style="left:442px">
    <div class="photo" role="img" aria-label="Team meeting in a bright city office" style="background:linear-gradient(135deg,#dfe8f2,#7c93ad)"></div>
    <div class="icon"><svg width="26" height="26" viewBox="0 0 24 24"><circle cx="12" cy="12" r="9" fill="none" stroke="#1e56a0" stroke-width="2"/><circle cx="12" cy="12" r="4" fill="#d9272e"/></svg></div>
    <h3>Account Based Marketing Leads (ABM)</h3>
    <p>ABM is a strategy that directs marketing resources to engaging a specific set of target accounts.</p>
    <p style="margin-top:8px">Instead of casting a wide net to engage any potential customers, marketers use ABM and work closely with sales to identify key prospects and then tailor customized programs and messages to the buying team within target accounts.</p>
    <div class="btn-outline">READ MORE <span>&#10230;</span></div>
  </article>
  <article class="card" style="left:796px">
    <div class="photo" role="img" aria-label="Hand selecting a verified profile on a digital screen" style="background:linear-gradient(135deg,#8aa2b6,#2f4d6a)"></div>
    <div class="icon"><svg width="26" height="26" viewBox="0 0 24 24"><path d="M5 5h14l-7 14z" fill="none" stroke="#d9272e" stroke-width="2"/><circle cx="12" cy="9" r="2" fill="#1e56a0"/></svg></div>
    <h3>Sales Qualified Lead / BANT</h3>
    <p>An SQL lead or a BANT lead is a type of lead that expressed a specific interest in a product and service that you have to offer...</p>
    <p style="margin-top:8px">The difference between marketing qualified leads (MQL) and sales qualified leads (SQL) is important to understanding your sales funnel, and perhaps most importantly, the potential bottlenecks within it.</p>
    <div class="btn-outline">READ MORE <span>&#10230;</span></div>
  </article>
</section>

<section class="qa">
  <div class="heading" style="top:108px">
    <div class="rule"><span></span><i></i></div><h2>QA Technology</h2><div class="rule"><i></i><span></span></div>
  </div>
  <div class="copy">
    <p>Brightfold Reach can deliver high quality sales leads from any country in the world. This can include leads via email or telemarketing, account-based targeting (ABM) or identifying need and pain points through BANT / SQL campaigns.</p>
    <p>Prospero is positioned to quickly identify, validate, and improve lead quality at the point-of-entry by filtering out all leads that do not match required filters, such as job title, company size, etc. The platform is designed to use real-time contact validation and live phone verification to remove all duplicate leads, as well as leads with invalid data components. Users can also build their own rules-based, post-submission verification protocol on our forms.</p>
    <p>Our goal is to provide the most accurate lead data to ensure the best opportunity for nurture and follow up by sales and marketing teams.</p>
    <span class="btn-solid">READ MORE <span>&#10230;</span></span>
  </div>
  <div class="product">PROSPERO</div>
</section>

<section class="intent">
  <div class="photo" role="img" aria-label="Hand with a pen reviewing printed data charts"></div>
  <div class="head"><h2>Intent Data</h2><div class="rule"><i></i><span></span></div></div>
  <div class="copy">
    <p>Our relationships with the world's most important technology &amp; business decisions-makers generate a perpetual stream of global data. With access to 35 million individuals and a global behavioural data stream that is authenticated, timely and contextually relevant, we have one of the industry's most powerful signals of buyer intent and can fuel your demand-generation marketing strategies globally.</p>
    <p>We support our Intent targeting capabilities by partnering with a number of third party intent providers, meaning we are able to target the global data universe to deliver the best and most engaging leads to our partners.</p>
    <span class="btn-solid">READ MORE <span>&#10230;</span></span>
  </div>
</section>

<section class="testimonials" role="img" aria-label="Dimmed photo of colleagues working at a table">
  <div class="heading" style="top:110px">
    <div class="rule"><span style="background:#fff"></span><i style="background:#fff"></i></div><h2>Client Testimonials</h2><div class="rule"><i style="background:#fff"></i><span style="background:#fff"></span></div>
  </div>
  <div class="quote" style="left:86px"><div class="mark">&ldquo;</div>Lorem ipsum dolor sit amet, cectetuer the adipiscing elit, sed diam nonummy nibh is lorem a euismod tincidunt ut laoreet dolore the magna is aliquam erat volutpat. Ut wisi enim ad minim the veniam, quis nostrud exerci tation le lorem the ullamcorper suscipit lobortis nisl ut.<div class="who"><b>DANIEL MARSH</b>Managing Director</div></div>
  <div class="quote" style="left:442px"><div class="mark">&ldquo;</div>Lorem ipsum dolor sit amet, cectetuer the adipiscing elit, sed diam nonummy nibh is lorem a euismod tincidunt ut laoreet dolore the magna is aliquam erat volutpat. Ut wisi enim ad minim the veniam, quis nostrud exerci tation le lorem the ullamcorper suscipit lobortis nisl ut.<div class="who"><b>PRIYA OKAFOR</b>Owner, Comapny Name</div></div>
  <div class="quote" style="left:797px"><div class="mark">&ldquo;</div>Lorem ipsum dolor sit amet, cectetuer the adipiscing elit, sed diam nonummy nibh is lorem a euismod tincidunt ut laoreet dolore the magna is aliquam erat volutpat. Ut wisi enim ad minim the veniam, quis nostrud exerci tation le lorem the ullamcorper suscipit lobortis nisl ut.<div class="who"><b>DANIEL MARSH</b>Marketing Manager</div></div>
</section>

<footer class="site-footer">
  <div class="col" style="left:90px">
    <h4>Quick Links <span class="rule"><span></span><i></i></span></h4>
    <ul><li>Home</li><li>About Us</li><li>Our Services</li><li>Prospero &amp; Qa Technology</li><li>Intent Data</li><li>Testimonials</li><li>Contact Us</li></ul>
  </div>
  <div class="col" style="left:322px">
    <h4>Contact Details <span class="rule"><span></span><i></i></span></h4>
    <div style="margin-top:30px">
      <div class="contact-row"><svg width="14" height="18" viewBox="0 0 24 30"><path d="M12 1a10 10 0 00-10 10c0 8 10 18 10 18s10-10 10-18A10 10 0 0012 1z" fill="#d9272e"/><circle cx="12" cy="11" r="4" fill="#fff"/></svg><div><b>Brightfold Reach</b>11, Street Name Lorem ipsum dolor sit amet<br>cectetuer the adipiscing elit - 012345</div></div>
      <div class="contact-row"><svg width="16" height="16" viewBox="0 0 24 24"><path fill="#1e56a0" d="M6.6 10.8a15 15 0 006.6 6.6l2.2-2.2a1 1 0 011-.25 11.4 11.4 0 003.6.6 1 1 0 011 1V20a1 1 0 01-1 1A17 17 0 013 4a1 1 0 011-1h3.5a1 1 0 011 1c0 1.25.2 2.45.6 3.6a1 1 0 01-.25 1z"/></svg>020-555-0147</div>
      <div class="contact-row"><svg width="16" height="16" viewBox="0 0 24 24"><rect x="5" y="2" width="14" height="7" fill="none" stroke="#1e56a0" stroke-width="2"/><rect x="2" y="9" width="20" height="9" fill="none" stroke="#1e56a0" stroke-width="2"/><rect x="6" y="15" width="12" height="7" fill="#fff" stroke="#1e56a0" stroke-width="2"/></svg>020-555-0147</div>
      <div class="contact-row"><svg width="16" height="14" viewBox="0 0 24 20"><rect x="1" y="1" width="22" height="18" rx="2" fill="none" stroke="#1e56a0" stroke-width="2"/><path d="M1 2l11 9 11-9" fill="none" stroke="#1e56a0" stroke-width="2"/></svg>info@brightfoldreach-example.com</div>
    </div>
  </div>
  <div class="col" style="left:678px">
    <h4>Quick Inquiry <span class="rule"><span></span><i></i></span></h4>
    <div style="margin-top:26px">
      <div class="field">Your Name</div><div class="field">Phone</div><div class="field">Email Address</div><div class="field tall">Message</div>
      <div class="submit">SUBMIT <span>&#9656;</span></div>
    </div>
  </div>
  <div class="col" style="left:1008px">
    <h4>Follow Us <span class="rule"><i></i></span></h4>
    <ul class="social" style="margin-top:14px"><li><i></i>Circlebook</li><li><i></i>Chirpline</li><li><i></i>Workly</li><li><i></i>Searchplus</li></ul>
  </div>
</footer>

<div class="copyright" style="position:absolute;left:0;width:1200px">Copyright © 2020 Brightfold Reach. All Rights Reserved.</div>

</body>
</html>
```